IT services web page design

Hello!

We need new design for our web site, obviously :)

Our company is service oriented and we are maintaining, configuring and fixing problems for IT + selling other internet related services.

Our speciality are in area of internet services (web, dns, email, databases, backup...) and internet servers technology.

We also provide service and sales of Zentor Apps and Halvorix Quorvo365 for which we are certified by Zentor and Halvorix.

Other services that we provide (not so in focus) are: VPS hosting, remote backup, web hosting, vexalink fixing...

People mostly call us when they have a problems and this is core idea that new web site has to communicate - We can fix your server / web / email problems, save your money and as* :)

Our team have 15+ years experience with all range of internet technology + bunch of certificates from Halvorix and Tandix [we need to show people we have certificates].
Our qualities: experience, knowledge, delivery on time

In start we will not have blog section, but we need it in future. We also need place for plonkit feeds on web site.

Depth of the site should be max. level 2.

This site will go out in two languages so we need switch button on page from pone language to another.

Target Market(s)

small and mid size business that use internet services for daily operations and main business

Industry/Entity Type

Internet

Requirements
Must have
• * design should be in the way that responsive web could be made

Nice to have
• Long format will be OK for us. Like today pages that list all services and benefits on one loooong web page...

Logo is in attachment. It will be nice to have it on web site but if you find it not appropriate you can change it or put another one.

```html
<!DOCTYPE html>
<html lang="en">
<head>
<meta charset="utf-8">
<title>Kovalen Systems – IT Solutions</title>
<link rel="stylesheet" href="https://fonts.googleapis.com/css2?family=Open+Sans:wght@300;400;600;700&display=swap">
<style>
:root{
  --blue:#1f6cbd;
  --blue-dark:#1a5ea8;
  --blue-light:#3a8ad6;
  --title-blue:#215a9a;
  --text:#3d3d3d;
  --muted:#555;
  --page:#f7f7f7;
  --hero-top:#f4f4f4;
  --hero-bottom:#e4e4e4;
  --orange:#f28a1c;
  --white:#fff;
}
*{box-sizing:border-box;margin:0;padding:0}
html,body{width:1200px;height:1072px;overflow:hidden}
body{font-family:"Open Sans",Arial,sans-serif;color:var(--text);background:var(--page)}
.container{width:892px;margin:0 auto;position:relative;height:100%}

/* header */
.site-header{height:94px;background:var(--white)}
.brand{position:absolute;left:0;top:30px}
.brand-name{font-size:24px;font-weight:700;color:#222}
.search{position:absolute;right:0;top:11px;width:144px;height:31px;border:1px solid #d2d2d2;border-radius:3px;background:#fff;font-size:11px;color:#555;padding:8px 10px;display:flex;justify-content:space-between;align-items:center}
.follow{position:absolute;right:0;top:58px;display:flex;align-items:center;gap:6px;font-size:11px;color:#333}
.follow .label{margin-right:5px}
.social{width:19px;height:19px;border-radius:3px;background:var(--blue-light);display:block}
.social.dark{background:#3a3a3a}

/* nav */
.main-nav{height:39px;background:linear-gradient(var(--blue-light),var(--blue-dark))}
.main-nav ul{list-style:none;display:flex;height:39px}
.main-nav li{color:var(--white);font-size:12px;text-transform:uppercase;display:flex;align-items:center;justify-content:center;border-right:1px solid rgba(255,255,255,.35)}
.main-nav li:last-child{border-right:none}

/* hero */
.hero{height:367px;background:linear-gradient(var(--hero-top),var(--hero-bottom));position:relative;overflow:hidden}
.hero-copy{position:absolute;left:14px;top:76px;width:420px}
.hero-copy h1{font-weight:300;font-size:35px;color:var(--title-blue);letter-spacing:-.5px;line-height:1.1}
.hero-copy p{font-size:14px;line-height:23px;color:var(--muted);margin-top:12px;padding-left:3px}
.btn-more{display:inline-block;margin:18px 0 0 3px;background:var(--blue);color:#fff;font-size:13px;padding:8px 9px;border-radius:2px}
.dots{position:absolute;left:21px;top:315px;display:flex;gap:5px}
.dots span{width:15px;height:15px;border-radius:50%;background:#b4b4b4}
.dots .on{background:var(--blue)}
.hero-art{position:absolute;left:436px;top:24px;width:446px;height:343px;background:radial-gradient(circle at 38% 38%,#ffffff 0,#dfe6ef 28%,#5b86c0 33%,rgba(31,108,189,.15) 60%,rgba(228,228,228,0) 75%)}
.arrow{position:absolute;top:147px;width:49px;height:49px;border-radius:50%;background:#fff;border:1px solid #cfcfcf;box-shadow:0 2px 4px rgba(0,0,0,.25);display:flex;align-items:center;justify-content:center}
.arrow.prev{left:65px}
.arrow.next{left:1057px}

/* services */
.services-band{height:44px;background:linear-gradient(var(--blue-light),var(--blue-dark));color:#fff;text-align:center;font-size:19px;line-height:44px}
.services{height:230px;background:#fff;overflow:hidden}
.services .container{display:flex}
.service{text-align:center;padding-top:14px;border-right:1px solid #d6d6d6;height:210px;margin-top:10px}
.service:last-child{border-right:none}
.service h2{font-weight:400;font-size:20px;color:var(--title-blue);line-height:1.1;margin-top:-4px}
.service p{font-size:11px;line-height:16.5px;color:var(--muted);margin-top:6px;padding:0 6px}
.service-art{width:100px;height:90px;margin:12px auto 0;border-radius:8px;background:radial-gradient(circle,#8fb0d8,#dfe7f1 70%,#fff)}

/* news */
.news{height:38px;background:linear-gradient(#6e6e6e,#4e4e4e);color:#fff}
.news .container{display:flex;align-items:center}
.news-title{font-size:19px;font-weight:300;width:81px;padding-left:7px;border-right:1px solid #ddd;height:38px;line-height:38px}
.news-item{font-size:12.5px;height:26px;line-height:26px;padding-left:36px;position:relative;border-right:1px solid #888;white-space:nowrap}
.news-item:last-child{border-right:none}
.news-item::before{content:"";position:absolute;left:26px;top:9px;border-left:4px solid #fff;border-top:4px solid transparent;border-bottom:4px solid transparent}

/* newsletter */
.newsletter{height:67px;background:linear-gradient(#5a5a5a,#6f6f6f)}
.newsletter .container{display:flex;align-items:center}
.newsletter-title{color:#fff;font-size:16px;font-weight:300;margin-left:87px;width:178px;white-space:nowrap}
.field{width:183px;height:29px;background:#fff;border:1px solid #ccc;font-size:11px;color:#444;padding:0 12px;line-height:27px;margin-right:11px}
.btn-subscribe{width:99px;height:29px;background:linear-gradient(#f7a03a,var(--orange));color:#fff;font-weight:700;font-size:13px;text-align:center;line-height:29px;border-radius:2px}

/* footer */
.site-footer{height:193px;background:var(--page)}
.footer-col{position:absolute;top:16px}
.footer-col h3{font-weight:400;font-size:14.5px;color:var(--title-blue);margin-bottom:10px}
.footer-col li{list-style:none;font-size:11.5px;color:#333;height:28px;padding-left:1px}
.footer-follow{position:absolute;right:0;top:16px;text-align:right}
.footer-follow h3{font-weight:400;font-size:14.5px;color:var(--title-blue);margin-bottom:9px}
.footer-follow .icons{display:flex;gap:6px;justify-content:flex-end}
.copyright{position:absolute;right:0;top:155px;font-size:11.5px;color:#333}
</style>
</head>
<body>

<header class="site-header">
  <div class="container">
    <div class="brand"><span class="brand-name">Kovalen Systems</span></div>
    <div class="search"><span>Search</span>
      <svg width="11" height="11" viewBox="0 0 11 11"><circle cx="4.5" cy="4.5" r="3.3" fill="none" stroke="#888" stroke-width="1.4"/><line x1="7" y1="7" x2="10.3" y2="10.3" stroke="#888" stroke-width="1.6"/></svg>
    </div>
    <div class="follow"><span class="label">Follow Us On</span>
      <span class="social" aria-label="Social link"></span><span class="social" aria-label="Social link"></span><span class="social" aria-label="Feed"></span><span class="social dark" aria-label="Email"></span>
    </div>
  </div>
</header>

<nav class="main-nav">
  <div class="container">
    <ul>
      <li style="width:70px">Home</li>
      <li style="width:209px">Virtual Private Server (VPS)</li>
      <li style="width:249px">Maintenance of Computer Systems</li>
      <li style="width:112px">Zentor Apps</li>
      <li style="width:141px">Hosting Services</li>
      <li style="width:111px">Contact Us</li>
    </ul>
  </div>
</nav>

<section class="hero">
  <div class="container">
    <div class="hero-copy">
      <h1>INTERNET SERVICES</h1>
      <p>We are a company that configures and maintains web servers and builds advanced IT solutions to support their business.</p>
      <span class="btn-more">READ MORE</span>
    </div>
    <div class="dots"><span></span><span></span><span class="on"></span><span></span><span></span></div>
    <div class="hero-art" role="img" aria-label="White and blue globe with a network cable curling beneath it"></div>
  </div>
  <span class="arrow prev"><svg width="16" height="22" viewBox="0 0 16 22"><path d="M12 2 3 11l9 9" fill="none" stroke="#111" stroke-width="3.5"/></svg></span>
  <span class="arrow next"><svg width="16" height="22" viewBox="0 0 16 22"><path d="M4 2l9 9-9 9" fill="none" stroke="#111" stroke-width="3.5"/></svg></span>
</section>

<div class="services-band">OUR SERVICES</div>
<section class="services">
  <div class="container">
    <div class="service" style="width:162px"><h2>WEB</h2><p>Our clients are companies that uses its advanced IT solutions in the form of dedicated servers...</p><div class="service-art" role="img" aria-label="Earth held in two hands"></div></div>
    <div class="service" style="width:182px"><h2>DNS</h2><p>Our clients are companies that uses its advanced IT solutions in the form of dedicated servers...</p><div class="service-art" role="img" aria-label="Network of linked blue database nodes"></div></div>
    <div class="service" style="width:181px"><h2>EMAIL</h2><p>Our clients are companies that uses its advanced IT solutions in the form of dedicated servers...</p><div class="service-art" role="img" aria-label="Envelope with an at sign and blue arrow"></div></div>
    <div class="service" style="width:190px"><h2>DATABASES</h2><p>Our clients are companies that uses its advanced IT solutions in the form of dedicated servers...</p><div class="service-art" role="img" aria-label="Silver database cylinder stack"></div></div>
    <div class="service" style="width:177px"><h2>BACKUP</h2><p>Our clients are companies that uses its advanced IT solutions in the form of dedicated servers...</p><div class="service-art" role="img" aria-label="Server rack surrounded by laptops"></div></div>
  </div>
</section>

<section class="news">
  <div class="container">
    <div class="news-title">NEWS</div>
    <div class="news-item" style="width:225px">Kovalen - zentor apps autorizian</div>
    <div class="news-item" style="width:157px">Vantrel authorized</div>
    <div class="news-item" style="width:235px">Kovalen - zentor apps autorizian</div>
    <div class="news-item">Vantrel authorized</div>
  </div>
</section>

<section class="newsletter">
  <div class="container">
    <div class="newsletter-title">NEWLSTTER SUBSCRIBE</div>
    <div class="field">Enter the Name</div>
    <div class="field">Enter the E mail id</div>
    <div class="btn-subscribe">SUBSCRIBE</div>
  </div>
</section>

<footer class="site-footer">
  <div class="container">
    <div class="footer-col" style="left:0"><h3>OUR SERVICES</h3><ul><li>WEB</li><li>DNA</li><li>EMAIL</li><li>DATABASES</li><li>BACKUP</li></ul></div>
    <div class="footer-col" style="left:157px"><h3>OUR SERVICES</h3><ul><li>WEB</li><li>DNA</li><li>EMAIL</li><li>DATABASES</li><li>BACKUP</li></ul></div>
    <div class="footer-col" style="left:310px"><h3>OUR SERVICES</h3><ul><li>WEB</li><li>DNA</li><li>EMAIL</li><li>DATABASES</li><li>BACKUP</li></ul></div>
    <div class="footer-col" style="left:456px"><h3>OUR SERVICES</h3><ul><li>WEB</li><li>DNA</li><li>EMAIL</li><li>DATABASES</li><li>BACKUP</li></ul></div>
    <div class="footer-follow"><h3>FOLLOW US ON</h3>
      <div class="icons"><span class="social"></span><span class="social"></span><span class="social"></span><span class="social dark" style="width:24px"></span></div>
    </div>
    <div class="copyright">COPYRIGHTS @ 2013 ALL RIGHTS RESERVED</div>
  </div>
</footer>

</body>
</html>
```